Business Card Design

Freelance writer, coach, teacher and researcher specialising in improving mathematics teaching and learning in primary schools. I write books and articles for teachers, speak extensively at conferences in UK and aboard. Would like something with a cube in the design. Clean, modern - logo suitable for use on a website. Should NOT look 'childish' (no comic sans or chalkboard type fonts)

Full details to go on card:

Professor Dale Voronin
Building Early Numeracy

info@dalevoronin.net
#dalevoronin26
www.dalevoronin.net
+44 7823 608 142

Industry/Entity Type

Teacher

Contact Information for Business Card

Professor Dale Voronin
Building Early Numeracy

```html
<!DOCTYPE html>
<html lang="en">
<head>
<meta charset="utf-8">
<title>Business Card – Professor Dale Voronin</title>
<link rel="stylesheet" href="https://fonts.googleapis.com/css2?family=Montserrat:wght@700&family=Questrial&display=swap">
<style>
  :root {
    --page-bg: #e9e7ef;
    --card-white: #ffffff;
    --ink: #1f1f24;
    --rule-blue: #2e3192;
    --lavender-light: #ece9f5;
    --lavender-mid: #c9c3e0;
    --lavender-deep: #aea6d1;
    --icon-blue: #3a3f9e;
  }
  * { margin: 0; padding: 0; box-sizing: border-box; }
  html, body {
    width: 1200px;
    height: 1000px;
    overflow: hidden;
    background: var(--page-bg);
  }
  .business-card {
    position: absolute;
    left: 100px;
    top: 220px;
    width: 1000px;
    height: 560px;
    background: var(--card-white);
    box-shadow: 0 10px 30px rgba(40, 35, 80, 0.18);
    overflow: hidden;
    font-family: "Questrial", "Century Gothic", sans-serif;
    color: var(--ink);
  }
  .card-backdrop {
    position: absolute;
    inset: 0;
  }
  .brand-mark {
    position: absolute;
    left: 70px;
    top: 190px;
    display: flex;
    align-items: center;
    gap: 18px;
  }
  .brand-mark__square {
    width: 64px;
    height: 64px;
    background: var(--rule-blue);
  }
  .brand-mark__name {
    font-family: "Questrial", "Century Gothic", sans-serif;
    font-weight: 400;
    font-size: 48px;
    letter-spacing: 1px;
    color: var(--ink);
    line-height: 1;
  }
  .identity {
    position: absolute;
    right: 70px;
    top: 78px;
    text-align: left;
  }
  .identity__name {
    font-family: "Montserrat", "Century Gothic", sans-serif;
    font-weight: 700;
    font-size: 40px;
    letter-spacing: 0.5px;
    line-height: 1.1;
  }
  .identity__tagline {
    font-size: 29px;
    letter-spacing: 0.6px;
    margin-top: 4px;
  }
  .contact-direct {
    position: absolute;
    right: 40px;
    top: 258px;
    text-align: right;
    font-size: 36px;
    line-height: 1.3;
    letter-spacing: 0.5px;
  }
  .contact-line {
    display: flex;
    align-items: center;
    justify-content: flex-end;
    gap: 12px;
  }
  .contact-online {
    position: absolute;
    left: 56px;
    top: 412px;
    font-size: 36px;
    line-height: 1.3;
    letter-spacing: 0.5px;
  }
  .contact-online .contact-line { justify-content: flex-start; }
  .icon { flex: none; }
</style>
</head>
<body>
  <div class="business-card">
    <svg class="card-backdrop" width="1000" height="560" viewBox="0 0 1000 560">
      <defs>
        <linearGradient id="facet-gradient" x1="0" y1="0" x2="1" y2="1">
          <stop offset="0" stop-color="#c9c3e0"/>
          <stop offset="0.45" stop-color="#ece9f5"/>
          <stop offset="1" stop-color="#aea6d1"/>
        </linearGradient>
      </defs>
      <polygon points="0,388 1000,196 1000,560 0,560" fill="url(#facet-gradient)" role="img" aria-label="Faceted lavender low-poly triangle pattern"/>
      <line x1="0" y1="388" x2="1000" y2="196" stroke="#2e3192" stroke-width="9"/>
    </svg>

    <div class="brand-mark">
      <div class="brand-mark__square"></div>
      <span class="brand-mark__name">DV</span>
    </div>

    <div class="identity">
      <div class="identity__name">Professor Dale Voronin</div>
      <div class="identity__tagline">Building Early Numeracy</div>
    </div>

    <div class="contact-direct">
      <div class="contact-line">
        <span>+44 7823 608 142</span>
        <svg class="icon" width="22" height="34" viewBox="0 0 22 34" aria-label="Phone">
          <rect x="2" y="2" width="18" height="30" rx="3" fill="none" stroke="#3a3f9e" stroke-width="2.5"/>
          <line x1="8" y1="27" x2="14" y2="27" stroke="#3a3f9e" stroke-width="2.5"/>
        </svg>
      </div>
      <div class="contact-line">
        <span>info@dalevoronin.net</span>
        <svg class="icon" width="34" height="24" viewBox="0 0 34 24" aria-label="Email">
          <rect x="2" y="2" width="30" height="20" fill="none" stroke="#3a3f9e" stroke-width="2.5"/>
          <polyline points="2,2 17,14 32,2" fill="none" stroke="#3a3f9e" stroke-width="2.5"/>
        </svg>
      </div>
    </div>

    <div class="contact-online">
      <div class="contact-line"><span>#dalevoronin26</span></div>
      <div class="contact-line">
        <svg class="icon" width="32" height="32" viewBox="0 0 32 32" aria-label="Website">
          <g fill="none" stroke="#3a3f9e" stroke-width="2.2">
            <circle cx="16" cy="16" r="13"/>
            <ellipse cx="16" cy="16" rx="6" ry="13"/>
            <line x1="3" y1="16" x2="29" y2="16"/>
            <line x1="5" y1="9" x2="27" y2="9"/>
            <line x1="5" y1="23" x2="27" y2="23"/>
          </g>
        </svg>
        <span>www.dalevoronin.net</span>
      </div>
    </div>
  </div>
</body>
</html>
```